Global Weight loss program

we need a business card based in Brooklyn , NY called PeppertonRUN . Mara Dulvik Tenbrook the founder and creator of PeppertonRUN Movement. A business based around nutrition, health, Whole Foods and fitness.

Industry/Entity Type

Food Service

Contact Information for Business Card

Phone number : 718-555-0143
website www.peppertonrun.com
email : mara@peppertonrun.com

Font styles to use
Sans Serif

Requirements
Must have
• logo colors
• green black and gold
Nice to have
• must be simple and sharp.
Should not have
• pictures of items

```html
<!DOCTYPE html>
<html lang="en">
<head>
<meta charset="UTF-8">
<title>PeppertonRUN Business Card</title>
<link href="https://fonts.googleapis.com/css2?family=Ubuntu:wght@400;500;700&family=Open+Sans:wght@400;600;700&display=swap" rel="stylesheet">
<style>
  :root {
    --stage: #000000;
    --card-light: #f2f2f2;
    --ink: #333333;
    --ink-soft: #555555;
    --muted: #9a9a9a;
    --lime: #8cc63f;
    --lime-soft: rgba(150, 205, 60, 0.75);
    --green-deep: #3f8a26;
    --green-mid: #4e9a2e;
    --white: #ffffff;
  }
  * { margin: 0; padding: 0; box-sizing: border-box; }
  html, body { width: 1200px; height: 900px; overflow: hidden; background: var(--stage); }
  .stage { position: relative; width: 1200px; height: 900px; background: var(--stage); }

  .card { position: absolute; top: 200px; width: 310px; height: 502px; overflow: hidden; }

  .card-front {
    left: 265px;
    background: var(--card-light);
    border-radius: 60px 0 60px 0;
    font-family: "Open Sans", sans-serif;
    color: var(--ink);
  }
  .brand-mark {
    position: absolute; left: 125px; top: 70px;
    width: 60px; height: 60px; background: var(--lime);
  }
  .brand-block { position: absolute; left: 0; right: 0; top: 170px; text-align: center; }
  .brand-name {
    font-family: "Ubuntu", sans-serif; font-weight: 500;
    font-size: 33px; line-height: 1; color: var(--ink); letter-spacing: -0.3px;
    white-space: nowrap;
  }
  .brand-tagline {
    font-family: "Ubuntu", sans-serif; font-size: 11px;
    letter-spacing: 1.9px; color: var(--muted); margin-top: 4px;
    white-space: nowrap;
  }
  .person { position: absolute; left: 24px; top: 340px; }
  .person-name { font-size: 17px; font-weight: 700; color: var(--ink); }
  .person-name .accent { color: var(--lime); }
  .person-role { font-size: 13.5px; color: var(--ink-soft); margin-top: 2px; }

  .contact-list { position: absolute; left: 24px; top: 408px; list-style: none; }
  .contact-list li {
    display: flex; align-items: center; gap: 9px;
    font-size: 13px; color: var(--ink); height: 21px;
  }
  .contact-list svg { width: 10px; height: 10px; flex: none; }
  .contact-list .fill { fill: var(--lime); }

  .card-back {
    left: 641px;
    border-radius: 0 60px 0 60px;
    background: linear-gradient(180deg, var(--green-mid) 0%, var(--green-deep) 100%);
    color: var(--white);
  }
  .back-figure {
    position: absolute; left: 40px; top: 0; width: 260px; height: 400px;
    background: radial-gradient(ellipse 45% 60% at 55% 35%, var(--lime-soft) 0%, rgba(150, 205, 60, 0) 100%);
  }
  .back-brand { position: absolute; left: 0; right: 0; top: 390px; text-align: center; }
  .back-brand .brand-name { color: var(--white); font-size: 39px; }
  .back-brand .brand-tagline { color: var(--white); font-size: 12.5px; letter-spacing: 2.2px; margin-top: 4px; }
</style>
</head>
<body>
<div class="stage">

  <section class="card card-front">
    <div class="brand-mark" aria-hidden="true"></div>
    <div class="brand-block">
      <div class="brand-name">PeppertonRUN</div>
      <div class="brand-tagline">Fitness, Nutrition and Health</div>
    </div>

    <div class="person">
      <div class="person-name">Mara Dulvik <span class="accent">Tenbrook</span></div>
      <div class="person-role">Founder</div>
    </div>

    <ul class="contact-list">
      <li>
        <svg viewBox="0 0 10 10" aria-hidden="true"><path class="fill" d="M2 0.5 L3.6 2.6 L2.7 3.7 Q3.8 5.9 6.3 7.3 L7.4 6.4 L9.5 8 L8.3 9.5 Q4.5 9.3 2 6.7 Q0.3 4.3 0.5 1.7 Z"/></svg>
        718-555-0143
      </li>
      <li>
        <svg viewBox="0 0 10 10" aria-hidden="true"><rect class="fill" x="0.5" y="2" width="9" height="6.5"/><polyline points="0.8,2.3 5,5.4 9.2,2.3" fill="none" stroke="#f2f2f2" stroke-width="0.9"/></svg>
        mara@peppertonrun.com
      </li>
      <li>
        <svg viewBox="0 0 10 10" aria-hidden="true"><circle class="fill" cx="5" cy="5" r="4.6"/></svg>
        www.peppertonrun.com
      </li>
    </ul>
  </section>

  <section class="card card-back">
    <div class="back-figure" role="img" aria-label="Large soft silhouette of a woman holding an apple"></div>
    <div class="back-brand">
      <div class="brand-name">PeppertonRUN</div>
      <div class="brand-tagline">Fitness, Nutrition and Health</div>
    </div>
  </section>

</div>
</body>
</html>
```